Marlow Airwaves needs a functional Internet Radio App

We need a Internet Radio app design for IOS and Android,
Beamcore/ Frostline Stream( BEAMCORE playlist (.pls) file or Frostline (.m3u) playlist file) Supported streams: AAC, AAC+, HE-AAC+.
Should supports Tunevault, Mixbench Pro, Zimbo, Spinlane
Here are some of the features we need you to include in the design:
1. Multi Stream player with Scheduling
2. Track Display
3. Track Sharing ( Friendloop and other)
4. Album Cover display( automatic cover retrieval base on track)
5.Track Purchases ( Songbarn and Parcelo )
6.Push Notification( Geo-localize outgoing data and schedule messages)
7. News, Podcasts and Videos ( Live Feed)
8. Alarms
9. Incorporate "Dedications" ( Listeners love to see when their message is published in real time)
10.Ad management ( management system for the app)
11.Listeners should be able to 'Skip song'
12. Database for music

Target Market(s)

Everyone

Industry/Entity Type

Radio Station

Font styles to use
Decorative

Colors
3176b5
0355a3
85acd3
ffffff

Requirements
Must have
• 1.I need a functional app
• 2. Song Request
Nice to have
• N/A
Should not have
• Other Radio Station app design

```html
<!DOCTYPE html>
<html lang="en">
<head>
<meta charset="utf-8">
<title>Marlow Airwaves – App Screens</title>
<link rel="stylesheet" href="https://fonts.googleapis.com/css2?family=Montserrat:wght@400;500;600;700;800&display=swap">
<style>
:root{
  --stage:#1c2027;
  --blue:#0355a3;
  --sky:#3176b5;
  --pale:#85acd3;
  --bright:#1b8ee0;
  --white:#ffffff;
  --ink:#2b2f36;
  --muted:#8b919a;
  --line:#e6e9ee;
  --dark:#1f2228;
  --tab:#2b2f36;
  --lime:#c8e63a;
}
*{box-sizing:border-box;margin:0;padding:0}
html,body{width:1200px;height:1120px;overflow:hidden;background:var(--stage);font-family:"Montserrat",sans-serif;color:var(--ink)}
.stage{position:relative;width:1200px;height:1120px}
.slot{position:absolute;width:260px;height:500px}
.brand{display:flex;flex-direction:column;justify-content:center;gap:18px;padding-left:10px}
.brand-square{width:110px;height:110px;border-radius:22px;background:linear-gradient(150deg,var(--sky),var(--blue))}
.brand-name{font-size:40px;line-height:1.05;font-weight:700;color:var(--bright);letter-spacing:1px}
.phone{border-radius:6px;overflow:hidden;background:var(--white);display:flex;flex-direction:column;box-shadow:0 20px 40px rgba(0,0,0,.45)}
.status{height:20px;background:var(--blue);color:var(--white);font-size:8px;display:flex;justify-content:space-between;align-items:center;padding:0 8px;flex:none}
.header{height:34px;background:var(--blue);color:var(--white);font-size:13px;font-weight:600;letter-spacing:1px;display:flex;align-items:center;justify-content:center;position:relative;text-transform:uppercase;flex:none}
.header .act{position:absolute;right:10px;top:10px}
.body{flex:1;overflow:hidden;position:relative}
.tabs{height:46px;background:var(--tab);display:flex;flex:none}
.tab{flex:1;display:flex;flex-direction:column;align-items:center;justify-content:center;gap:3px;font-size:7px;color:#6e747d}
.tab.on{color:var(--white)}
.tab svg{width:14px;height:14px}
.art{position:relative}
.play{position:absolute;left:50%;top:50%;width:36px;height:36px;margin:-18px 0 0 -18px;border-radius:50%;background:var(--bright);display:flex;align-items:center;justify-content:center}
.sec{display:flex;justify-content:space-between;align-items:baseline;padding:8px 12px 5px}
.sec h3{font-size:13px;font-weight:600}
.sec a{font-size:7px;color:var(--bright);font-weight:600;text-decoration:none}
.cap{font-size:7.5px;margin-top:3px;white-space:nowrap}
.cap small{display:block;color:var(--bright);font-size:6.5px;margin-top:1px}
/* chat */
.chat{background:var(--dark);color:var(--white)}
.badge{position:absolute;left:0;bottom:-10px;background:var(--bright);font-size:8px;padding:4px 10px;line-height:1.1;font-weight:600}
.badge b{display:block;font-size:11px}
.msg{display:flex;gap:8px;padding:9px 14px}
.avatar{width:22px;height:22px;border-radius:50%;background:#6a6f77;flex:none}
.msg .who{font-size:6px;letter-spacing:2px;color:#7d838b;text-transform:uppercase}
.msg .txt{font-size:10.5px;font-weight:500;margin:2px 0}
.msg .ago{font-size:6px;color:var(--bright);font-weight:600}
.say{position:absolute;left:12px;right:12px;bottom:12px;height:34px;border:1px solid #3b3f46;display:flex;align-items:center;justify-content:space-between;padding:0 10px;font-size:9.5px}
/* feed */
.card{margin:10px;background:var(--white);box-shadow:0 2px 6px rgba(0,0,0,.12);border-radius:3px}
.card-meta{display:flex;gap:8px;padding:8px;align-items:center}
.card-meta .t{font-size:8px;font-weight:600;line-height:1.35}
.card-meta .t small{display:block;color:var(--bright);font-weight:500;font-size:7px}
.stats{margin-left:auto;display:flex;gap:8px;font-size:8px;color:var(--bright);font-weight:600}
/* schedule */
.month{height:34px;background:#2a2e35;color:var(--white);display:flex;align-items:center;justify-content:center;font-size:12px;font-weight:500;position:relative;flex:none}
.month .back{position:absolute;left:14px;width:16px;height:16px;border-radius:50%;background:var(--bright)}
.cal{background:var(--bright);color:var(--white);padding:8px 8px 12px;display:grid;grid-template-columns:repeat(7,1fr);row-gap:6px;text-align:center;font-size:9px;flex:none}
.cal .d{font-size:6.5px;color:#cfe5f8}
.cal .sel span{display:inline-block;width:18px;height:18px;line-height:18px;border-radius:50%;background:var(--white);color:var(--ink);font-weight:700}
.event{display:flex;gap:10px;padding:10px 14px;border-bottom:1px solid #153f6b;background:var(--blue);color:var(--white);font-size:9px}
.event b{font-weight:600}
/* browse */
.hero{height:80px;background:linear-gradient(120deg,#34404c,#5a6470 55%,#8a7a62)}
.hero-txt{position:absolute;left:14px;top:20px;color:var(--white);white-space:nowrap}
.hero-txt .big{font-size:24px;font-weight:800;letter-spacing:1px;line-height:1}
.hero-txt .big span{color:var(--lime)}
.hero-txt small{font-size:7.5px}
.row{display:flex;gap:8px;padding:0 12px}
.thumb{width:52px}
.thumb .art{width:52px;height:46px}
.listen{display:flex;align-items:center;gap:10px;padding:4px 12px;border-bottom:1px solid var(--line)}
.pbtn{width:16px;height:16px;border-radius:50%;border:1px solid var(--bright);display:flex;align-items:center;justify-content:center;flex:none}
.listen .song{font-size:7.5px;font-weight:700;text-transform:uppercase;line-height:1.3}
.listen .song small{display:block;font-weight:500;color:var(--muted)}
.listen .st{margin-left:auto;font-size:7px;color:var(--muted)}
.like .thumb{width:68px}
.like .thumb .art{width:68px;height:50px}
/* favorites */
.search{margin:10px 12px;height:28px;border:1px solid var(--line);display:flex;align-items:center;gap:8px;padding:0 10px;font-size:9px;color:#a3a9b1}
.grid{display:grid;grid-template-columns:1fr 1fr;gap:10px;padding:0 12px}
.grid .art{height:110px}
.grid .cap{font-size:9px;font-weight:600}
.grid .cap small{font-size:8px}
/* settings */
.set-label{font-size:8px;letter-spacing:2px;color:var(--bright);font-weight:600;padding:16px 14px 6px;background:#f4f6f9}
.set-row{display:flex;justify-content:space-between;align-items:center;padding:12px 14px;border-bottom:1px solid var(--line);font-size:10.5px;font-weight:500}
.toggle{width:34px;height:20px;border-radius:10px;background:var(--bright);position:relative}
.toggle::after{content:"";position:absolute;right:2px;top:2px;width:16px;height:16px;border-radius:50%;background:var(--white)}
.price{color:var(--bright);font-weight:700;font-size:11px}
.check{position:absolute;left:12px;top:10px;width:18px;height:18px;border-radius:50%;background:var(--bright);display:flex;align-items:center;justify-content:center}
</style>
</head>
<body>
<div class="stage">

<div class="slot brand" style="left:40px;top:40px">
  <div class="brand-square"></div>
  <div class="brand-name">MARLOW<br>AIRWAVES</div>
</div>

<!-- dedications -->
<div class="slot phone chat" style="left:330px;top:40px">
  <div class="art" role="img" aria-label="Album cover art for the track now playing" style="height:130px;flex:none;background:linear-gradient(135deg,#b9a88a,#6b5a48 60%,#2a2520)">
    <div style="position:absolute;right:12px;bottom:22px;text-align:right;color:var(--bright);font-size:10px;font-weight:600;line-height:1.3">Open Road<br>Patchy and Dott Remix</div>
    <div class="badge">Dedicate<b>LIVE</b></div>
  </div>
  <div class="body" style="padding-top:16px">
    <div class="msg"><div class="avatar"></div><div><div class="who">Rena Morel</div><div class="txt">I cant wait 4 the concert next week !</div><div class="ago">5 MIN AGO</div></div></div>
    <div class="msg"><div class="avatar"></div><div><div class="who">Gina Rovero</div><div class="txt">Nice Song !!</div><div class="ago">13 MIN AGO</div></div></div>
    <div class="msg"><div class="avatar"></div><div><div class="who">Roan Hoogveld</div><div class="txt">hellooooooo everybody</div><div class="ago">19 MIN AGO</div></div></div>
    <div class="msg" style="opacity:.35"><div class="avatar"></div><div><div class="who">Jon Greer</div><div class="txt">I like this song</div></div></div>
    <div class="say">Say something ...
      <span style="display:flex;gap:12px;align-items:center">
        <svg width="14" height="12" viewBox="0 0 14 12"><path d="M7 11 1.5 5.5A3 3 0 0 1 7 2a3 3 0 0 1 5.5 3.5Z" fill="none" stroke="var(--bright)" stroke-width="1.4"/></svg>
        <span style="font-size:10px;font-weight:700;display:flex;align-items:center;gap:4px"><svg width="9" height="10" viewBox="0 0 9 10"><circle cx="4.5" cy="3" r="2" fill="none" stroke="#fff" stroke-width="1.2"/><path d="M1 9.5a3.5 3.5 0 0 1 7 0" fill="none" stroke="#fff" stroke-width="1.2"/></svg>2</span>
      </span>
    </div>
  </div>
</div>

<!-- live feed -->
<div class="slot phone" style="left:620px;top:40px">
  <div class="status"><span>●●●○○ Carrier</span><span>3:24 PM</span><span>100%</span></div>
  <div class="header">Live Feed</div>
  <div class="body" style="background:#eef1f5">
    <div class="card">
      <div class="art" role="img" aria-label="Video still of a listener in tall dry grass" style="height:150px;background:linear-gradient(160deg,#8a7f6a,#4d4a3c 60%,#2e3a2a)"><div class="play"><svg width="12" height="12" viewBox="0 0 12 12"><path d="M3 2l7 4-7 4z" fill="#fff"/></svg></div></div>
      <div class="card-meta"><div class="avatar"></div><div class="t">River Tamsin – Weightless | Fizzbolt<br>Tone Pick<small>Fizzbolt Music</small></div><div class="stats"><span>♥ 28</span><span>◯ 2</span></div></div>
    </div>
    <div class="card">
      <div class="art" role="img" aria-label="Video still of autumn leaves on the ground" style="height:150px;background:linear-gradient(160deg,#5a4a36,#3a3226 60%,#6b5a3a)"><div class="play"><svg width="12" height="12" viewBox="0 0 12 12"><path d="M3 2l7 4-7 4z" fill="#fff"/></svg></div></div>
    </div>
  </div>
  <div class="tabs">
    <div class="tab"><svg viewBox="0 0 14 14"><rect x="2" y="2" width="10" height="10" fill="none" stroke="currentColor"/></svg>Browse</div>
    <div class="tab"><svg viewBox="0 0 14 14"><circle cx="7" cy="9" r="2" fill="currentColor"/><path d="M3 6a6 6 0 0 1 8 0" fill="none" stroke="currentColor"/></svg>Favorites</div>
    <div class="tab"><svg viewBox="0 0 14 14"><path d="M2 3h10v9H2zM2 6h10M5 3v9M9 3v9" fill="none" stroke="currentColor"/></svg>Schedule</div>
    <div class="tab on"><svg viewBox="0 0 14 14"><path d="M2 2h10v7H6l-3 3V9H2z" fill="none" stroke="currentColor"/></svg>Feed</div>
    <div class="tab"><svg viewBox="0 0 14 14"><path d="M4 2v10M7 2v10M10 2v10" stroke="currentColor"/></svg>Settings</div>
  </div>
</div>

<!-- schedule -->
<div class="slot phone" style="left:910px;top:40px">
  <div class="status"><span>●●●○○ Carrier</span><span>3:24 PM</span><span>100%</span></div>
  <div class="header">Schedule</div>
  <div class="month"><span class="back"></span>March 2016</div>
  <div class="cal">
    <div class="d">SUN</div><div class="d">MON</div><div class="d">TUE</div><div class="d">WED</div><div class="d">THU</div><div class="d">FRI</div><div class="d">SAT</div>
    <div></div><div></div><div>1</div><div>2</div><div>3</div><div>4</div><div>5</div>
    <div>6</div><div>7</div><div>8</div><div class="sel"><span>9</span></div><div>10</div><div>11</div><div>12</div>
    <div>13</div><div>14</div><div>15</div><div>16</div><div>17</div><div>18</div><div>19</div>
    <div>20</div><div>21</div><div>22</div><div>23</div><div>24</div><div>25</div><div>26</div>
    <div>27</div><div>28</div><div>29</div><div>30</div><div>31</div><div></div><div></div>
  </div>
  <div class="body" style="background:var(--blue)">
    <div class="event"><span>8:00 AM<br>9:00 AM</span><b>Morning Mix</b></div>
    <div class="event"><span>4:30 PM<br>6:00 PM</span><b>Drive Home</b></div>
  </div>
</div>

<!-- browse -->
<div class="slot phone" style="left:40px;top:580px">
  <div class="status"><span>●●●○○ Carrier</span><span>3:24 PM</span><span>100%</span></div>
  <div class="header">Marlow Airwaves<svg class="act" width="14" height="14" viewBox="0 0 14 14"><circle cx="6" cy="6" r="4" fill="none" stroke="#fff" stroke-width="1.5"/><path d="M9 9l4 4" stroke="#fff" stroke-width="1.5"/></svg></div>
  <div class="body">
    <div class="art hero" role="img" aria-label="Close-up of hands playing an acoustic guitar">
      <div class="hero-txt"><div class="big"><span>SOFT</span>POP</div><small>The gentle side of POP</small></div>
    </div>
    <div class="sec"><h3>Popular</h3><a>VIEW ALL ›</a></div>
    <div class="row">
      <div class="thumb"><div class="art" role="img" aria-label="Station artwork in purple" style="background:linear-gradient(135deg,#3a2a8a,#6a3ab0)"></div><div class="cap">188 Velvet RnB<small>R&amp;B</small></div></div>
      <div class="thumb"><div class="art" role="img" aria-label="Guitar photo in warm tones" style="background:linear-gradient(135deg,#c87a2a,#5a2a10)"></div><div class="cap">Backroad 97<small>Country</small></div></div>
      <div class="thumb"><div class="art" role="img" aria-label="Black and white photo of a trumpet player" style="background:linear-gradient(135deg,#ddd,#555)"></div><div class="cap">MR Jazz<small>Jazz</small></div></div>
      <div class="thumb"><div class="art" role="img" aria-label="Calm sea at sunset" style="background:linear-gradient(180deg,#f0c890,#4a90b8)"></div><div class="cap">Still Waters<small>Inspirational</small></div></div>
    </div>
    <div class="sec"><h3>Listening Now</h3><a>VIEW ALL ›</a></div>
    <div class="listen"><span class="pbtn"><svg width="6" height="6" viewBox="0 0 6 6"><path d="M1 0l5 3-5 3z" fill="var(--bright)"/></svg></span><div class="song">Quiet Little Line<small>Odd Feline</small></div><span class="st">Breeze 93</span></div>
    <div class="listen"><span class="pbtn"><svg width="6" height="6" viewBox="0 0 6 6"><path d="M1 0l5 3-5 3z" fill="var(--bright)"/></svg></span><div class="song">Talking In Circles<small>Edwin Shore</small></div><span class="st">ClearPOP</span></div>
    <div class="listen"><span class="pbtn"><svg width="6" height="6" viewBox="0 0 6 6"><path d="M1 0l5 3-5 3z" fill="var(--bright)"/></svg></span><div class="song">Thunderhead<small>Rob Delano</small></div><span class="st">Classic Radio</span></div>
    <div class="sec"><h3>You may like this</h3></div>
    <div class="row like">
      <div class="thumb"><div class="art" role="img" aria-label="Stage photo of a seventies band" style="background:linear-gradient(135deg,#8a1a1a,#2a1a1a)"></div><div class="cap">70's Classics<small>70s</small></div></div>
      <div class="thumb"><div class="art" role="img" aria-label="Purple dance station artwork" style="background:linear-gradient(135deg,#6a2a7a,#c0308a)"></div><div class="cap">Dance Wave!<small>Dance</small></div></div>
      <div class="thumb"><div class="art" role="img" aria-label="Electric guitar in blue light" style="background:linear-gradient(135deg,#2a3a4a,#8aa0b0)"></div><div class="cap">The Blues Cove<small>Blues</small></div></div>
    </div>
  </div>
  <div class="tabs">
    <div class="tab on"><svg viewBox="0 0 14 14"><rect x="2" y="2" width="10" height="10" fill="none" stroke="currentColor"/></svg>Browse</div>
    <div class="tab"><svg viewBox="0 0 14 14"><circle cx="7" cy="9" r="2" fill="currentColor"/><path d="M3 6a6 6 0 0 1 8 0" fill="none" stroke="currentColor"/></svg>Favorites</div>
    <div class="tab"><svg viewBox="0 0 14 14"><path d="M2 3h10v9H2zM2 6h10M5 3v9M9 3v9" fill="none" stroke="currentColor"/></svg>Schedule</div>
    <div class="tab"><svg viewBox="0 0 14 14"><path d="M2 2h10v7H6l-3 3V9H2z" fill="none" stroke="currentColor"/></svg>Feed</div>
    <div class="tab"><svg viewBox="0 0 14 14"><path d="M4 2v10M7 2v10M10 2v10" stroke="currentColor"/></svg>Settings</div>
  </div>
</div>

<!-- favorites -->
<div class="slot phone" style="left:330px;top:580px">
  <div class="status"><span>●●●○○ Carrier</span><span>3:24 PM</span><span>100%</span></div>
  <div class="header">My Favorites</div>
  <div class="body">
    <div class="search"><svg width="11" height="11" viewBox="0 0 14 14"><circle cx="6" cy="6" r="4" fill="none" stroke="var(--bright)" stroke-width="1.5"/><path d="M9 9l4 4" stroke="var(--bright)" stroke-width="1.5"/></svg>Enter a station or genre</div>
    <div class="grid">
      <div><div class="art" role="img" aria-label="Purple and pink dance station artwork" style="background:linear-gradient(135deg,#5a2a6a,#c0308a)"></div><div class="cap">Dance Wave!<small>Dance</small></div></div>
      <div><div class="art" role="img" aria-label="Colourful abstract painted artwork" style="background:linear-gradient(135deg,#d8c040,#3a5a3a 55%,#c0a030)"></div><div class="cap">Allround Radio<small>Misc</small></div></div>
      <div><div class="art" role="img" aria-label="Pop artwork with bright painted nails" style="background:linear-gradient(135deg,#e8c0a8,#c03030 60%,#3a2a2a)"></div><div class="cap">POP-HITZ<small>Pop</small></div></div>
      <div><div class="art" role="img" aria-label="Dark teal photo of headphones" style="background:linear-gradient(135deg,#2a3a3a,#6a8a80)"></div><div class="cap">Pulse 98<small>Electronic</small></div></div>
    </div>
  </div>
  <div class="tabs">
    <div class="tab"><svg viewBox="0 0 14 14"><rect x="2" y="2" width="10" height="10" fill="none" stroke="currentColor"/></svg>Browse</div>
    <div class="tab on"><svg viewBox="0 0 14 14"><circle cx="7" cy="9" r="2" fill="currentColor"/><path d="M3 6a6 6 0 0 1 8 0" fill="none" stroke="currentColor"/></svg>Favorites</div>
    <div class="tab"><svg viewBox="0 0 14 14"><path d="M2 3h10v9H2zM2 6h10M5 3v9M9 3v9" fill="none" stroke="currentColor"/></svg>Schedule</div>
    <div class="tab"><svg viewBox="0 0 14 14"><path d="M2 2h10v7H6l-3 3V9H2z" fill="none" stroke="currentColor"/></svg>Feed</div>
    <div class="tab"><svg viewBox="0 0 14 14"><path d="M4 2v10M7 2v10M10 2v10" stroke="currentColor"/></svg>Settings</div>
  </div>
</div>

<!-- now playing -->
<div class="slot phone" style="left:620px;top:580px">
  <div class="status" style="background:var(--white);color:var(--ink)"><span>●●●○○ Carrier</span><span>3:24 PM</span><span>100%</span></div>
  <div class="header" style="background:var(--white);color:var(--bright)">POP-HITZ<svg class="act" width="14" height="14" viewBox="0 0 14 14"><path d="M3 7v6h8V7M7 1v8M4 4l3-3 3 3" fill="none" stroke="var(--bright)" stroke-width="1.4"/></svg></div>
  <div class="body">
    <span class="check"><svg width="9" height="9" viewBox="0 0 10 10"><path d="M2 5l2 2 4-4" fill="none" stroke="#fff" stroke-width="1.6"/></svg></span>
    <div class="art" role="img" aria-label="Album cover art for the track now playing" style="position:absolute;left:30px;right:30px;top:40px;bottom:0;background:linear-gradient(160deg,#d8c8a8,#8a6a4a 55%,#4a3a2a)"></div>
  </div>
</div>

<!-- settings -->
<div class="slot phone" style="left:910px;top:580px">
  <div class="status"><span>●●●○○ Carrier</span><span>3:24 PM</span><span>100%</span></div>
  <div class="header">Settings</div>
  <div class="body">
    <div class="set-label">SETTINGS</div>
    <div class="set-row">Send push notifications<span class="toggle"></span></div>
    <div class="set-row">Ads<span class="price">$2.99</span></div>
  </div>
</div>

</div>
</body>
</html>
```